Design the 1st of 6 postcards marketing government software

We sell permit software to government agencies and need an eye catching postcard for our direct mailing campaign. This will be the first card in a series of 6. Designs should use our company color palette found in the attached "logo master details.pdf" and resemble our website design at terranexa.com. The postcard should have a modern and minimalistic feel and should use imagery of "small town main street" such as the attached "retail-store" photo. The front of the card should display the headline "Automate Your Plan Review Workflow and Cut Review Times In Half" and feature our logo. The back of the card should prominently display our website "TerraNexa.com" and also feature our 4 products as seen in the solutions section of our home page (Citizen Access, Plan Review, Permits, Inspections). You can use the same 4 icons but don't include the lengthy descriptions. two .indd files have been included as a template for the size of the card and blank space required on the back. Also include our phone number 1 (833) 527-3149 x3 and email sales@terranexa.com on the back of the card, you can optionally use our pin icon as a watermark in the background, it can be oversized and run of the page if you want, similar to the trusted clients section of our home page.

```html
<!DOCTYPE html>
<html lang="en">
<head>
<meta charset="utf-8">
<title>TerraNexa Postcard 1 – Front and Back</title>
<link rel="stylesheet" href="https://fonts.googleapis.com/css2?family=Montserrat:wght@600&family=Open+Sans:wght@700&family=Raleway:wght@400&family=Roboto:wght@500&display=swap">
<style>
  :root {
    --brand-blue: #3b86e0;
    --navy: #111c38;
    --ink: #161616;
    --band-black: #0f1115;
    --white: #ffffff;
    --text-grey: #2a2a2a;
    --page: #ffffff;
  }
  * { margin: 0; padding: 0; box-sizing: border-box; }
  html, body { width: 1200px; height: 1179px; overflow: hidden; background: var(--page); }
  .stage { position: relative; width: 1200px; height: 1179px; }

  /* ---------- Front ---------- */
  .card-front { position: absolute; left: 31px; top: 49px; width: 751px; height: 604px; background: var(--white); }
  .front-edge { position: absolute; left: 0; top: 0; width: 30px; height: 100%; background: var(--brand-blue); }
  .front-logo-box { position: absolute; left: 30px; top: 0; width: 295px; height: 138px; background: var(--white);
    display: flex; align-items: center; justify-content: center; }
  .front-panel { position: absolute; left: 30px; top: 138px; width: 295px; height: 466px; background: var(--navy); }
  .headline { position: absolute; left: 0; top: 42px; width: 100%; text-align: center; color: var(--white);
    font-family: "Open Sans", sans-serif; font-weight: 700; font-size: 36.5px; line-height: 37.5px; letter-spacing: -1.3px; }
  .front-photo { position: absolute; left: 325px; top: 0; width: 426px; height: 604px;
    background: linear-gradient(180deg, #1f7fe0 0%, #4a9be6 30%, #8fb6d6 48%, #b8a595 60%, #6d5a52 75%, #2a2a30 100%); }

  .wordmark { font-family: "Montserrat", sans-serif; font-weight: 600; color: var(--ink); letter-spacing: 0.5px;
    display: flex; align-items: center; gap: 7px; }
  .wordmark .dot { width: 8px; height: 8px; border-radius: 50%; background: var(--brand-blue); }
  .front-logo-box .wordmark { font-size: 24px; }

  /* ---------- Back ---------- */
  .card-back { position: absolute; left: 483px; top: 552px; width: 663px; height: 570px; background: var(--white); }
  .back-logo { position: absolute; left: 0; top: 16px; width: 100%; display: flex; justify-content: center; }
  .back-logo .wordmark { font-size: 16px; }
  .device-showcase { position: absolute; left: 165px; top: 58px; width: 360px; height: 230px; border-radius: 8px;
    background: linear-gradient(180deg, #2b3a5c 0%, #1f2b48 60%, #e9ecf1 61%, #f4f5f7 100%); }
  .solutions-band { position: absolute; left: 0; top: 298px; width: 100%; height: 40px; background: var(--band-black);
    color: var(--white); font-family: "Raleway", sans-serif; font-size: 19px; letter-spacing: 3.4px;
    display: flex; align-items: center; justify-content: center; }
  .products { position: absolute; left: 35px; top: 367px; width: 610px; display: grid;
    grid-template-columns: repeat(4, 1fr); gap: 6px; }
  .product-head { display: flex; align-items: center; gap: 10px; margin-bottom: 11px; }
  .product-icon { width: 22px; height: 22px; flex: none; }
  .product-name { font-family: "Raleway", sans-serif; font-size: 14.5px; color: var(--ink); }
  .product-copy { font-family: "Raleway", sans-serif; font-size: 8.6px; line-height: 12.8px; color: var(--text-grey); width: 124px; }
  .contact-bar { position: absolute; left: 0; bottom: 0; width: 100%; height: 66px; background: var(--brand-blue);
    color: var(--white); font-family: "Roboto", sans-serif; font-weight: 500; font-size: 13.5px;
    display: flex; align-items: center; justify-content: center; gap: 12px; }
</style>
</head>
<body>
<div class="stage">

  <section class="card-front">
    <div class="front-edge"></div>
    <div class="front-logo-box">
      <div class="wordmark"><span>TerraNexa</span><span class="dot"></span></div>
    </div>
    <div class="front-panel">
      <h1 class="headline">Automate<br>Your Plan<br>Review<br>Workflow<br>and cut<br>Review Times<br>In Half!</h1>
    </div>
    <div class="front-photo" role="img" aria-label="Photo of a small town main street at sunset with brick buildings, street lamps and a blue sky"></div>
  </section>

  <section class="card-back">
    <div class="back-logo">
      <div class="wordmark"><span>TerraNexa</span><span class="dot"></span></div>
    </div>
    <div class="device-showcase" role="img" aria-label="Laptop and phone displaying the TerraNexa website homepage"></div>
    <div class="solutions-band">Innovative Solutions Designed For You</div>

    <div class="products">
      <div class="product">
        <div class="product-head">
          <svg class="product-icon" viewBox="0 0 24 24" fill="none" stroke="#222" stroke-width="1.2">
            <rect x="5" y="3" width="14" height="12"/><path d="M2 20h20l-3-5H5z"/><path d="M9 7h6M9 10h6"/>
          </svg>
          <span class="product-name">Citizen Acess</span>
        </div>
        <p class="product-copy">Provide applicants a 24/7, one-stop shop for the information related to their projects — all without having to call or come into the office to get the information.</p>
      </div>
      <div class="product">
        <div class="product-head">
          <svg class="product-icon" viewBox="0 0 24 24" fill="none" stroke="#222" stroke-width="1.2">
            <rect x="3" y="4" width="18" height="14"/><path d="M6 15l4-5 3 3 5-6"/><path d="M8 22l4-4 4 4"/>
          </svg>
          <span class="product-name">Plan Review</span>
        </div>
        <p class="product-copy">Reduce turnaround times and streamline your collaboration with applicants through centralized commenting and concurrent reviews.</p>
      </div>
      <div class="product">
        <div class="product-head">
          <svg class="product-icon" viewBox="0 0 24 24" fill="none" stroke="#222" stroke-width="1.2">
            <rect x="4" y="2" width="13" height="18"/><path d="M7 6h7M7 9h7M7 12h7"/><rect x="9" y="14" width="11" height="8"/>
          </svg>
          <span class="product-name">Permit</span>
        </div>
        <p class="product-copy">Create, track, automate, and manage permits and other documents with ease.</p>
      </div>
      <div class="product">
        <div class="product-head">
          <svg class="product-icon" viewBox="0 0 24 24" fill="none" stroke="#222" stroke-width="1.2">
            <rect x="3" y="3" width="14" height="18"/><path d="M6 7h8M6 10h4"/><circle cx="14" cy="14" r="4"/><path d="M17 17l4 4"/>
          </svg>
          <span class="product-name">Inspection</span>
        </div>
        <p class="product-copy">Take your inspection to the field and access our full suite of inspection features with any mobile device.</p>
      </div>
    </div>

    <div class="contact-bar">
      <span>1 (833) 527-3149</span><span>|</span><span>sales@terranexa.com</span><span>|</span><span>www.terranexa.com</span>
    </div>
  </section>

</div>
</body>
</html>
```